Business Card Design needed for start up company Pramora

In need of a new business card designed for a start up company based in Sydney, Pramora is a new start up innovative Company, our mission it to make property accessible for everyday Australian and to become the leading Real Estate platform in Australia. We want it to be fresh and clean.

Industry/Entity Type

Financial

Contact Information for Business Card

Section for Name
Section for Title

PRAMORA - Where Doors Open Wide
Mobile:
Direct:

Font styles to use
Sans Serif

Colors
33a6d7
0692cd
0255a3
ffffff

Requirements
Must have
• Logo, all business card details

```html
<!DOCTYPE html>
<html lang="en">
<head>
<meta charset="utf-8">
<title>Pramora Business Card</title>
<link rel="stylesheet" href="https://fonts.googleapis.com/css2?family=Arimo:wght@400;700&display=swap">
<style>
  :root {
    --sky: #33a6d7;
    --azure: #0692cd;
    --royal: #0255a3;
    --navy: #1d3565;
    --white: #ffffff;
    --paper: #f4f5f6;
    --ink-dark: #12284f;
    --stage: #2b2b2d;
  }
  * { box-sizing: border-box; margin: 0; padding: 0; }
  html, body {
    width: 1200px; height: 997px; overflow: hidden;
    background: var(--stage);
    font-family: "Arimo", Arial, sans-serif;
  }
  .canvas { position: relative; width: 1200px; height: 997px; }
  .card {
    position: absolute; width: 660px; height: 377px;
    border-radius: 18px; overflow: hidden;
    background: linear-gradient(160deg, var(--white), var(--paper));
    box-shadow: 0 14px 40px rgba(0,0,0,.45);
  }
  .card-front { left: 90px; top: 90px; }
  .card-back { left: 450px; top: 520px; }

  .wordmark {
    position: absolute; left: 0; right: 0; text-align: center;
    font-weight: 400; color: var(--azure); line-height: 1;
    letter-spacing: 6px;
  }
  .card-front .wordmark { top: 140px; font-size: 60px; }
  .card-back .wordmark { top: 74px; font-size: 48px; }

  .tagline {
    position: absolute; left: 0; right: 0; top: 228px; text-align: center;
    font-size: 15px; letter-spacing: 2px; color: var(--royal);
  }

  .bands { position: absolute; inset: 0; }
  .holder {
    position: absolute; left: 150px; width: 410px; top: 184px; text-align: center;
  }
  .holder-name { font-size: 22px; letter-spacing: 1px; color: var(--white); }
  .holder-title { font-size: 13px; color: var(--ink-dark); margin-top: 2px; }

  .address {
    position: absolute; right: 28px; top: 238px; text-align: right;
    font-style: normal; font-size: 14px; line-height: 1.4; color: var(--white);
  }
  .contacts { position: absolute; left: 26px; top: 272px; list-style: none; }
  .contacts li {
    display: flex; align-items: center; gap: 10px;
    font-size: 15px; letter-spacing: .5px; color: var(--white); height: 25px;
  }
  .contacts svg { width: 16px; height: 16px; flex: none; }
</style>
</head>
<body>
<main class="canvas">

  <section class="card card-front" aria-label="Card front">
    <p class="wordmark">Pramora</p>
    <p class="tagline">WHERE DOORS OPEN WIDE</p>
  </section>

  <section class="card card-back" aria-label="Card back">
    <p class="wordmark">Pramora</p>

    <svg class="bands" viewBox="0 0 660 377" preserveAspectRatio="none" aria-hidden="true">
      <polygon points="0,242 170,212 440,212 490,168 660,150 660,377 0,377" fill="var(--sky)"/>
      <polygon points="0,256 180,228 450,228 500,184 660,168 660,377 0,377" fill="var(--navy)"/>
      <polygon points="150,228 190,178 520,178 560,228" fill="var(--azure)"/>
      <polygon points="0,362 660,340 660,377 0,377" fill="var(--sky)"/>
    </svg>

    <div class="holder">
      <p class="holder-name">LENA HARTWELL</p>
      <p class="holder-title">Fashion Retailer</p>
    </div>

    <address class="address">
      18 Harbour Lane, Upper Ridge Road<br>
      Sydney, NSW, Australia
    </address>

    <ul class="contacts">
      <li>
        <svg viewBox="0 0 16 16"><circle cx="8" cy="8" r="8" fill="var(--sky)"/><path d="M5 4.5h2l.6 2-1 .8a5 5 0 0 0 2.1 2.1l.8-1 2 .6v2a1 1 0 0 1-1 1A6.5 6.5 0 0 1 4 5.5a1 1 0 0 1 1-1z" fill="var(--white)"/></svg>
        +61 400 555 018
      </li>
      <li>
        <svg viewBox="0 0 16 16"><circle cx="8" cy="8" r="8" fill="var(--sky)"/><rect x="5.5" y="3.5" width="5" height="9" rx="1" fill="var(--white)"/></svg>
        +61 400 555 027
      </li>
      <li>
        <svg viewBox="0 0 16 16"><circle cx="8" cy="8" r="8" fill="var(--sky)"/><rect x="4" y="5" width="8" height="6" fill="var(--white)"/><path d="M4 5l4 3.5L12 5" stroke="var(--sky)" fill="none"/></svg>
        lena.h@pramora.example
      </li>
    </ul>
  </section>

</main>
</body>
</html>
```